Verdell Chiropractic, achieve your health goals, get better each day one step at a time

A mobile friendly site, fresh look, easy to navigate, has interface with pw/chirply, etc. Blog posts. Uses new logo. Content and address to current site is mirvaton.com. The current site will give you scope of project for content. The logo is not the final but close. Will upload final next week.
Convey the concept that heath is a process, it does not just happen. We take steps to achieve what we want in life including health.

Target Market(s)

30 to 70 year old. Needing health care

Industry/Entity Type

Health Care

Coding

Coded - Design and coding required

Number of Pages Required

5+ page

Font styles to use
Sans Serif

Colors

Designer to choose colors to be used in the design.

Requirements
Must have
• mobile friendly, easy to navigate, PW/Chirply interface, blog, room for current content
Nice to have
• potential for commerce, statistics
Should not have
• Same old look and feel as everything else out there

```html
<!DOCTYPE html>
<html lang="en">
<head>
<meta charset="utf-8">
<title>Verdell Chiropractic – Better Health Care</title>
<link rel="stylesheet" href="https://fonts.googleapis.com/css2?family=Source+Sans+3:wght@300;400;600;700&display=swap">
<style>
  :root {
    --lavender: #a487c9;
    --lavender-soft: rgba(164, 135, 201, 0.88);
    --white: #ffffff;
    --ink: #1d1d1f;
    --hero-dark: #2b2a2e;
    --hero-mid: #4f4a4c;
    --hero-warm: #6a5a4e;
    --hero-blue: #2f3c5c;
    --page-bg: #dedede;
  }
  * { box-sizing: border-box; margin: 0; padding: 0; }
  html, body {
    width: 1200px; height: 800px; overflow: hidden;
    background: var(--page-bg);
    font-family: "Source Sans 3", "Helvetica Neue", Arial, sans-serif;
  }
  .site { position: relative; width: 1200px; height: 800px; overflow: hidden; }

  /* Header */
  .site-header {
    position: absolute; inset: 0 0 auto 0; height: 110px;
    background: var(--lavender); color: var(--white);
  }
  .utility-bar {
    position: absolute; top: 14px; right: 96px;
    display: flex; align-items: center; gap: 14px;
  }
  .social-list { display: flex; gap: 10px; list-style: none; }
  .social-item {
    display: flex; align-items: center; gap: 5px;
    font-size: 12px; font-weight: 400; color: var(--white);
  }
  .social-item::before {
    content: ""; width: 9px; height: 9px; border-radius: 50%; background: var(--white);
  }
  .search-field {
    display: flex; align-items: center; justify-content: space-between;
    width: 300px; margin-left: 18px; padding-bottom: 3px;
    border-bottom: 1px solid rgba(255,255,255,0.75);
    font-size: 15px; font-weight: 300;
  }
  .brand {
    position: absolute; left: 70px; top: 66px;
    font-size: 26px; font-weight: 300; letter-spacing: 0.5px;
  }
  .main-nav {
    position: absolute; right: 96px; top: 72px;
    display: flex; gap: 24px; list-style: none;
    font-size: 15px; font-weight: 300;
  }

  /* Hero */
  .hero { position: absolute; top: 110px; left: 0; width: 1200px; height: 690px; }
  .hero-photo {
    position: absolute; inset: 0;
    background:
      radial-gradient(ellipse 420px 300px at 30% 70%, rgba(120,100,85,0.55), transparent 70%),
      radial-gradient(ellipse 380px 320px at 72% 40%, rgba(47,60,92,0.7), transparent 70%),
      linear-gradient(180deg, var(--hero-mid) 0%, var(--hero-dark) 100%);
  }
  .hero-shade { position: absolute; inset: 0; background: rgba(20,18,22,0.35); }
  .hero-copy {
    position: absolute; top: 255px; left: 0; width: 100%;
    text-align: center; color: var(--white);
  }
  .hero-title { font-size: 46px; font-weight: 400; letter-spacing: 0.5px; word-spacing: 8px; }
  .hero-lede { margin-top: 14px; font-size: 22px; font-weight: 300; }

  /* Appointment card */
  .appointment {
    position: absolute; left: 340px; bottom: 0; width: 520px; height: 170px;
    background: var(--lavender-soft);
    padding: 24px 60px 0;
  }
  .appointment-grid {
    display: grid; grid-template-columns: 1fr 1fr; gap: 9px 10px;
  }
  .field {
    height: 24px; background: var(--white); color: var(--ink);
    font-size: 12px; font-weight: 600; padding: 4px 12px;
  }
  .field-wide { grid-column: 1 / -1; }
  .appointment-submit {
    grid-column: 1 / -1; height: 24px; background: var(--white); color: var(--ink);
    font-size: 12px; font-weight: 600; text-align: center; padding-top: 4px;
  }
</style>
</head>
<body>
<div class="site">
  <header class="site-header">
    <div class="utility-bar">
      <ul class="social-list">
        <li class="social-item">pw</li>
        <li class="social-item">chirply</li>
        <li class="social-item">netlane</li>
      </ul>
      <div class="search-field">
        <span>Search</span>
        <svg width="14" height="14" viewBox="0 0 14 14" aria-hidden="true">
          <circle cx="5.5" cy="5.5" r="4.3" fill="none" stroke="#fff" stroke-width="1.4"/>
          <line x1="8.7" y1="8.7" x2="13" y2="13" stroke="#fff" stroke-width="1.4"/>
        </svg>
      </div>
    </div>
    <div class="brand">LOGO</div>
    <ul class="main-nav">
      <li>Home</li>
      <li>Meet Doctor</li>
      <li>Testimonials</li>
      <li>FAQS</li>
      <li>Resources</li>
      <li>Contact</li>
    </ul>
  </header>

  <section class="hero">
    <div class="hero-photo" role="img" aria-label="Photo of a clinician in blue scrubs checking an elderly patient's blood pressure"></div>
    <div class="hero-shade"></div>
    <div class="hero-copy">
      <h1 class="hero-title">Better Health Care</h1>
      <p class="hero-lede">Lorem Ipsum is simply dummy text of the printing and typesetting</p>
    </div>

    <form class="appointment">
      <div class="appointment-grid">
        <div class="field field-wide">Name</div>
        <div class="field">Phone</div>
        <div class="field">Email</div>
        <div class="field">Select Date</div>
        <div class="field">Time</div>
        <div class="appointment-submit">Make an appointment</div>
      </div>
    </form>
  </section>
</div>
</body>
</html>
```